QUICK: Fresh Ideas for New Home Page Design!

Simply improve on our home page design and provide PSD file.

We are Sunward Coverage, a trusted health insurance comparison site to make shopping and enrolling in Carewell easy. We are certified agents for Pacific Shield Exchange, the state's health insurance marketplace (logo attached).

Use flat UI colors.

Looking for a fun design. Reference websites are:
www.plumvista.com
www.hibrindle.com
www.tolmex.com
www.findcanopy.com
www.trymeadowcoverplan.com

Target Market(s)

Individuals ages 18 - 64 shopping for health insurance for themselves and/or their family members. California residents. Don't have health insurance and want it or have it and looking to change.

Industry/Entity Type

Shopping

Font styles to use
Sans Serif

Colors
faed22
33a6d7
33b7a4

Requirements
Must have
• No stock photos. No medical or doctor images or photos. Use images of families. Friendly. Modern fonts and flat UI colors.
Nice to have
• Create a mock-up logo for Sunward Coverage.
Should not have
• No stock looking photos or images

```html
<!DOCTYPE html>
<html lang="en">
<head>
<meta charset="utf-8">
<title>Health Plans</title>
<link href="https://fonts.googleapis.com/css2?family=Open+Sans:wght@300;400;600;700&display=swap" rel="stylesheet">
<style>
:root{
  --blue:#3b8fd8;
  --blue-dark:#2f7cc4;
  --heading-blue:#4b8fcf;
  --green:#55d58a;
  --text:#333;
  --muted:#888;
  --light:#aaa;
  --white:#fff;
  --footer:#6e6e6e;
  --footer-dark:#565656;
  --footer-text:#e6e6e6;
}
*{box-sizing:border-box;margin:0;padding:0}
html,body{width:1200px;height:3000px;overflow:hidden}
body{font-family:"Open Sans",sans-serif;color:var(--text);background:var(--white);position:relative}
.abs{position:absolute}

.topbar{left:0;top:0;width:1200px;height:32px;background:var(--blue);color:var(--white);font-size:11px}
.topbar .call{left:150px;top:9px}
.topbar .social{left:300px;top:9px;display:flex;gap:10px}
.topbar .social span{width:13px;height:13px;border-radius:50%;background:rgba(255,255,255,.85);display:block}
.topbar .util{left:908px;top:0;display:flex;height:32px}
.topbar .util div{padding:9px 26px;border-left:1px solid rgba(255,255,255,.3)}
.topbar .util div:last-child{border-right:1px solid rgba(255,255,255,.3)}

.navbar{left:0;top:32px;width:1200px;height:76px;background:var(--white)}
.brand{left:130px;top:22px;display:flex;align-items:center;gap:10px;font-size:23px;font-weight:600;color:var(--blue-dark)}
.brand i{width:22px;height:22px;border:3px solid var(--blue-dark);display:block}
.menu{top:0;height:76px;font-size:14px;font-weight:600;color:#555}
.menu a{position:absolute;top:30px;white-space:nowrap;text-decoration:none;color:inherit}
.menu a.active{color:var(--blue)}
.menu a.active::after{content:"";position:absolute;left:-4px;right:-4px;top:42px;height:3px;background:var(--blue)}

.hero{left:0;top:108px;width:1200px;height:456px;background:linear-gradient(120deg,#8fb6e0 0%,#c9d9ea 35%,#a7c2e2 60%,#6f9fd6 100%)}
.hero h1{left:0;width:1200px;top:118px;text-align:center;color:var(--white);font-size:44px;font-weight:600}
.hero p{left:0;width:1200px;top:176px;text-align:center;color:var(--white);font-size:22px}
.hero p b{color:var(--green);font-weight:400}
.btn-ghost{border:2px solid var(--white);color:var(--white);font-size:17px;font-weight:600;text-align:center;border-radius:3px}
.hero .btn-ghost{left:522px;top:238px;width:156px;height:46px;line-height:42px}

.categories{left:0;top:564px;width:1200px;height:170px}
.cat{top:24px;width:120px;text-align:center}
.cat svg{display:block;margin:0 auto}
.cat .name{font-size:15px;font-weight:600;color:var(--blue-dark);margin-top:6px}
.cat .sub{font-size:10px;color:var(--light);margin-top:2px}
.arrow{top:52px}

.help{left:0;top:734px;width:1200px;height:378px;background:linear-gradient(90deg,#ececec,#f6f6f6 50%,#e2e2e2)}
.help h2{left:132px;top:50px;font-size:34px;font-weight:300;color:var(--heading-blue)}
.help p{left:132px;top:106px;width:520px;font-size:13px;line-height:29px;color:#666}
.btn-line{border:2px solid var(--blue-dark);color:var(--blue-dark);font-size:16px;border-radius:3px;text-align:center}
.help .btn-line{left:132px;top:248px;width:140px;height:38px;line-height:34px}
.help .portrait{left:754px;top:0;width:300px;height:378px;background:linear-gradient(180deg,#d8cfc6,#7a7a80 70%,#5c5c62)}

.simple{left:0;top:1112px;width:1200px;height:604px}
.simple h2{left:0;width:1200px;top:48px;text-align:center;font-size:36px;font-weight:300;color:var(--heading-blue)}
.simple .lead{left:0;width:1200px;top:100px;text-align:center;font-size:16px;color:var(--muted)}
.person{width:400px;height:100px}
.person .avatar{left:0;top:0;width:100px;height:100px;border-radius:50%;background:linear-gradient(160deg,#e4d8cf,#b9a89d);border:4px solid #f1f1f1}
.person h3{left:124px;top:18px;font-size:16px;font-weight:600;color:#333}
.person p{left:124px;top:44px;width:240px;font-size:12px;line-height:21px;color:var(--muted)}
.simple .btn-line{left:528px;top:524px;width:142px;height:38px;line-height:34px}

.reform{left:0;top:1716px;width:1200px;height:482px;background:linear-gradient(180deg,#9ec0dd,#b5cde2 45%,#8eb1d3)}
.reform h2{left:0;width:1200px;top:46px;text-align:center;font-size:36px;font-weight:300;color:var(--white)}
.reform .lead{left:0;width:1200px;top:96px;text-align:center;font-size:16px;color:#8ea9c4}
.feature{top:194px;width:220px;text-align:center}
.feature .icon{width:92px;height:92px;margin:0 auto;border-radius:8px;background:linear-gradient(180deg,#fff,#e6e6e6)}
.feature h3{margin-top:26px;font-size:16px;font-weight:600;color:var(--white)}
.feature p{margin-top:4px;font-size:12px;line-height:21px;color:#d6e4f1}

.partners{left:0;top:2198px;width:1200px;height:482px}
.partners h2{left:0;width:1200px;top:44px;text-align:center;font-size:36px;font-weight:300;color:var(--heading-blue)}
.partner{width:200px;text-align:center;font-size:20px;font-weight:600;color:#4d6b8c}

.footer{left:0;top:2680px;width:1200px;height:250px;background:var(--footer);color:var(--footer-text)}
.footer h4{font-size:23px;font-weight:400;color:var(--white)}
.col{top:34px}
.col ul{list-style:none;margin-top:14px}
.col li{font-size:11px;line-height:22.5px}
.col li::before{content:"- ";}
.contact li{list-style:none;display:flex;gap:18px;font-size:11px;line-height:19px;margin-bottom:14px;width:260px}
.contact li::before{content:none}
.contact svg{flex:none;margin-top:2px}
.copyright{left:0;top:2930px;width:1200px;height:70px;background:var(--footer-dark);color:var(--footer-text);text-align:center;font-size:10px;line-height:14px;padding-top:10px}
.copyright .main{font-size:11px;color:var(--white);margin-bottom:4px}
</style>
</head>
<body>

<header class="topbar abs">
  <div class="call abs">Call: 800-555-0143</div>
  <div class="social abs"><span></span><span></span><span></span><span></span></div>
  <div class="util abs"><div>Chat</div><div>Help</div></div>
</header>

<nav class="navbar abs">
  <div class="brand abs"><i></i>Logo Here</div>
  <div class="menu abs">
    <a class="active" style="left:464px">Home</a>
    <a style="left:562px">Health Plans</a>
    <a style="left:710px">Health Benefits</a>
    <a style="left:872px">About Us</a>
    <a style="left:988px">Contact Us</a>
  </div>
</nav>

<section class="hero abs" role="img" aria-label="Smiling family of four close together, tinted blue">
  <h1 class="abs">We have the health plan for you</h1>
  <p class="abs"><b>13,000+</b> plans from <b>180+</b> carriers</p>
  <div class="btn-ghost abs">Get Quotes</div>
</section>

<section class="categories abs">
  <svg class="arrow abs" style="left:132px" width="16" height="24" viewBox="0 0 16 24"><path d="M12 3 4 12l8 9" fill="none" stroke="#666" stroke-width="3"/></svg>
  <svg class="arrow abs" style="left:1054px" width="16" height="24" viewBox="0 0 16 24"><path d="M4 3l8 9-8 9" fill="none" stroke="#666" stroke-width="3"/></svg>

  <div class="cat abs" style="left:156px">
    <svg width="74" height="74" viewBox="0 0 74 74"><circle cx="37" cy="37" r="35" fill="none" stroke="#3b8fd8" stroke-width="3"/><path d="M30 18h14v12h12v14H44v12H30V44H18V30h12z" fill="#3b8fd8"/></svg>
    <div class="name">Medicare</div><div class="sub">Insurance</div>
  </div>
  <div class="cat abs" style="left:310px">
    <svg width="74" height="74" viewBox="0 0 74 74"><circle cx="37" cy="37" r="35" fill="none" stroke="#3b8fd8" stroke-width="3"/><path d="M37 16v44" stroke="#3b8fd8" stroke-width="4"/><path d="M22 26h30" stroke="#3b8fd8" stroke-width="4" stroke-linecap="round"/><circle cx="37" cy="17" r="4" fill="#3b8fd8"/></svg>
    <div class="name">Health</div><div class="sub">Insurance</div>
  </div>
  <div class="cat abs" style="left:462px">
    <svg width="74" height="74" viewBox="0 0 74 74"><circle cx="37" cy="37" r="35" fill="none" stroke="#3b8fd8" stroke-width="3"/><path d="M37 56 20 39a10 10 0 0 1 17-14 10 10 0 0 1 17 14z" fill="none" stroke="#3b8fd8" stroke-width="4"/><path d="M22 38h9l3-6 4 10 3-4h11" fill="none" stroke="#3b8fd8" stroke-width="2.5"/></svg>
    <div class="name">Life</div><div class="sub">Insurance</div>
  </div>
  <div class="cat abs" style="left:618px">
    <svg width="74" height="74" viewBox="0 0 74 74"><circle cx="37" cy="37" r="35" fill="none" stroke="#3b8fd8" stroke-width="3"/><circle cx="37" cy="26" r="8" fill="#3b8fd8"/><path d="M21 56c0-12 7-18 16-18s16 6 16 18z" fill="#3b8fd8"/></svg>
    <div class="name">Accident</div><div class="sub">Insurance</div>
  </div>
  <div class="cat abs" style="left:770px">
    <svg width="74" height="74" viewBox="0 0 74 74"><circle cx="37" cy="37" r="35" fill="none" stroke="#3b8fd8" stroke-width="3"/><circle cx="37" cy="39" r="15" fill="none" stroke="#3b8fd8" stroke-width="4"/><path d="M37 31v9h7" fill="none" stroke="#3b8fd8" stroke-width="3"/><path d="M24 22l-4 4M50 22l4 4" stroke="#3b8fd8" stroke-width="4"/></svg>
    <div class="name">short term</div><div class="sub">Insurance</div>
  </div>
  <div class="cat abs" style="left:922px">
    <svg width="74" height="74" viewBox="0 0 74 74"><circle cx="37" cy="37" r="35" fill="none" stroke="#3b8fd8" stroke-width="3"/><circle cx="37" cy="37" r="17" fill="none" stroke="#3b8fd8" stroke-width="4"/><path d="M37 28v10h7" fill="none" stroke="#3b8fd8" stroke-width="3"/></svg>
    <div class="name">Long term</div><div class="sub">Insurance</div>
  </div>
</section>

<section class="help abs">
  <h2 class="abs">We're Here to Help</h2>
  <p class="abs">Lorem Ipsum is simply dummy text of the printing and typesetting industry. Lorem Ipsum has been the industry's standard dummy text ever since the 1500s, when an unknown printer took a galley of type and scrambled it to make a type specimen book. It has survived not only five centuries.</p>
  <div class="btn-line abs">Read more &#9655;</div>
  <div class="portrait abs" role="img" aria-label="Smiling insurance advisor in a grey business suit with arms crossed"></div>
</section>

<section class="simple abs">
  <h2 class="abs">Health insurance doesn't have to be complicated</h2>
  <p class="lead abs">Lorem Ipsum is simply dummy text of the printing and typesetting industry.</p>
  <div class="person abs" style="left:210px;top:190px"><div class="avatar abs" role="img" aria-label="Portrait of a smiling man"></div><h3 class="abs">Lorem Ipsum name</h3><p class="abs">There are many variations of passages of Lorem Ipsum available.</p></div>
  <div class="person abs" style="left:648px;top:190px"><div class="avatar abs" role="img" aria-label="Portrait of a bald man"></div><h3 class="abs">Lorem Ipsum name</h3><p class="abs">There are many variations of passages of Lorem Ipsum available.</p></div>
  <div class="person abs" style="left:210px;top:354px"><div class="avatar abs" role="img" aria-label="Portrait of a smiling woman"></div><h3 class="abs">Lorem Ipsum name</h3><p class="abs">There are many variations of passages of Lorem Ipsum available.</p></div>
  <div class="person abs" style="left:648px;top:354px"><div class="avatar abs" role="img" aria-label="Portrait of a woman"></div><h3 class="abs">Lorem Ipsum name</h3><p class="abs">There are many variations of passages of Lorem Ipsum available.</p></div>
  <div class="btn-line abs">Get Started</div>
</section>

<section class="reform abs">
  <h2 class="abs">All About Health Reform</h2>
  <p class="lead abs">simply dummy text.</p>
  <div class="feature abs" style="left:154px"><div class="icon" role="img" aria-label="Rotary telephone dial icon"></div><h3>Lorem Ipsum</h3><p>There are many variations of<br>passages of Lorem Ipsum.</p></div>
  <div class="feature abs" style="left:378px"><div class="icon" role="img" aria-label="Shopping bag icon"></div><h3>Lorem Ipsum</h3><p>There are many variations of<br>passages of Lorem Ipsum.</p></div>
  <div class="feature abs" style="left:600px"><div class="icon" role="img" aria-label="Open envelope with letter icon"></div><h3>Lorem Ipsum</h3><p>There are many variations of<br>passages of Lorem Ipsum.</p></div>
  <div class="feature abs" style="left:826px"><div class="icon" role="img" aria-label="Book with bookmark icon"></div><h3>Lorem Ipsum</h3><p>There are many variations of<br>passages of Lorem Ipsum.</p></div>
</section>

<section class="partners abs">
  <h2 class="abs">Choices for affordable health coverage</h2>
  <div class="partner abs" style="left:166px;top:178px">Northgate Health</div>
  <div class="partner abs" style="left:400px;top:178px">Amberline Health</div>
  <div class="partner abs" style="left:636px;top:178px">Crestway</div>
  <div class="partner abs" style="left:850px;top:178px">Harborview Plan</div>
  <div class="partner abs" style="left:166px;top:318px">Westfield Care</div>
  <div class="partner abs" style="left:400px;top:318px">Lumora</div>
  <div class="partner abs" style="left:636px;top:318px">Brookdale Plan</div>
  <div class="partner abs" style="left:850px;top:318px">Tessaly Health</div>
</section>

<footer class="footer abs">
  <div class="col abs" style="left:130px"><h4>Services</h4><ul><li>Medical Plans by State</li><li>Health Insurance Companies</li><li>Find a Doctor</li><li>Other Languages</li><li>Mobile</li><li>Customer Service</li></ul></div>
  <div class="col abs" style="left:370px"><h4>Company</h4><ul><li>About Us</li><li>Careers</li><li>Licensing and Legal</li><li>Privacy Policy</li><li>Affiliate Program</li></ul></div>
  <div class="col abs" style="left:576px"><h4>Products</h4><ul><li>Health Insurance</li><li>Medicare</li><li>Maternity Coverage</li><li>PPO Plans</li><li>HMO Plans</li><li>Plumvista Medicare</li></ul></div>
  <div class="col contact abs" style="left:800px"><h4>Contact Us</h4><ul>
    <li><svg width="16" height="14" viewBox="0 0 16 14"><path d="M8 0 0 7h2v7h4V9h4v5h4V7h2z" fill="#fff"/></svg><span>Lorem Ipsum is simply dummy text of the printing 48548.</span></li>
    <li><svg width="16" height="12" viewBox="0 0 16 12"><rect width="16" height="12" fill="#fff"/><path d="M0 0l8 6 8-6" fill="none" stroke="#6e6e6e" stroke-width="1.5"/></svg><span>info@lindquay.com</span></li>
    <li><svg width="16" height="16" viewBox="0 0 16 16"><path d="M3 1l3 3-2 2c1 2 3 4 5 5l2-2 3 3-2 3C7 15 1 9 1 3z" fill="#fff"/></svg><span>(09) 555 0182 &nbsp;/ &nbsp;021 555019</span></li>
  </ul></div>
</footer>

<div class="copyright abs">
  <div class="main">Copyright © 2014 Company name.All rights reserved.</div>
  <div>"Pacific Shield Exchange" and the Pacific Shield Exchange Logo are registered trademarks or service marks of Pacific Shield Exchange, in the United States.</div>
  <div>This website is owned and maintained by Brightlake Insurance Services, Inc., which is solely responsible for its content. This site is not maintained by or affiliated with Pacific Shield Exchange.</div>
</div>

</body>
</html>
```